Bref créative
R.T. M&P Stationary
Simple
Odel Krasniak
7281 Porravel Blvd.
Suite 382
Porravel Heights, CA 95555
odel@tinmarrowseek.com
www.tinmarrowseek.com

```html
<!DOCTYPE html>
<html lang="en">
<head>
<meta charset="utf-8">
<title>R.T. M&amp;P Stationary — Business Card</title>
<link rel="stylesheet" href="https://fonts.googleapis.com/css2?family=Montserrat:wght@400;600&family=Open+Sans:wght@400;600&display=swap">
<style>
  :root {
    --page: #ecebe7;
    --gold: #c8a75a;
    --gold-deep: #b8954a;
    --cream: #f6e9c4;
    --cream-soft: #ead7a0;
    --shadow: rgba(60, 45, 20, 0.18);
  }
  * { box-sizing: border-box; margin: 0; padding: 0; }
  html, body {
    width: 1200px; height: 629px; overflow: hidden;
    background: var(--page);
  }
  .stage {
    width: 1200px; height: 629px;
    display: flex; align-items: center; justify-content: center; gap: 60px;
  }
  .card {
    position: relative;
    width: 500px; height: 286px;
    background: var(--gold);
    box-shadow: 0 10px 24px var(--shadow);
    overflow: hidden;
    color: var(--cream);
    font-family: "Open Sans", sans-serif;
  }
  .brand {
    display: flex; align-items: center; gap: 12px;
  }
  .brand-dot {
    width: 34px; height: 34px; border-radius: 50%;
    background: var(--cream);
  }
  .brand-name {
    font-family: "Montserrat", sans-serif;
    font-weight: 600;
    color: var(--cream);
    letter-spacing: 0.04em;
  }
  .card-front .brand {
    position: absolute; left: 50%; top: 50%;
    transform: translate(-50%, -50%);
  }
  .card-front .brand-dot { width: 54px; height: 54px; }
  .card-front .brand-name { font-size: 40px; }

  .card-back .brand {
    position: absolute; left: 34px; top: 40px;
  }
  .card-back .brand-name { font-size: 24px; }
  .contact-list {
    position: absolute; right: 34px; top: 40px;
    list-style: none;
    font-size: 9.5px; line-height: 1;
  }
  .contact-list li {
    display: flex; align-items: center; gap: 7px;
    margin-bottom: 7px;
  }
  .contact-list svg { width: 11px; height: 11px; flex: none; }
  .holder-name {
    position: absolute; left: 0; right: 0; top: 142px;
    text-align: center;
    font-size: 12px; font-weight: 600; letter-spacing: 0.03em;
  }
  .address {
    position: absolute; left: 34px; bottom: 38px;
    font-size: 9.5px; line-height: 1.45;
  }
  .waves {
    position: absolute; left: 0; bottom: 0;
    width: 500px; height: 120px;
  }
</style>
</head>
<body>
<main class="stage">
  <section class="card card-front" aria-label="Card front">
    <div class="brand">
      <span class="brand-dot"></span>
      <span class="brand-name">R.T. M&amp;P</span>
    </div>
  </section>

  <section class="card card-back" aria-label="Card back">
    <div class="brand">
      <span class="brand-dot"></span>
      <span class="brand-name">R.T. M&amp;P</span>
    </div>

    <ul class="contact-list">
      <li>
        <svg viewBox="0 0 12 12"><circle cx="6" cy="6" r="6" fill="var(--cream)"/><path d="M4 3.2l1 1.6-.6.7c.4.9 1 1.5 1.9 1.9l.7-.6 1.6 1-.5 1c-2.6-.2-4.4-2-4.6-4.6z" fill="var(--gold)"/></svg>
        (555) 014-2287
      </li>
      <li>
        <svg viewBox="0 0 12 12"><circle cx="6" cy="6" r="6" fill="var(--cream)"/><rect x="4.2" y="2.8" width="3.6" height="6.4" rx=".6" fill="var(--gold)"/></svg>
        (555) 014-3391
      </li>
      <li>
        <svg viewBox="0 0 12 12"><circle cx="6" cy="6" r="6" fill="var(--cream)"/><rect x="3" y="4" width="6" height="4.2" fill="var(--gold)"/><path d="M3 4l3 2.4L9 4" stroke="var(--cream)" stroke-width=".6" fill="none"/></svg>
        odel@tinmarrowseek.com
      </li>
      <li>
        <svg viewBox="0 0 12 12"><circle cx="6" cy="6" r="6" fill="var(--cream)"/><circle cx="6" cy="6" r="3" fill="none" stroke="var(--gold)" stroke-width=".8"/><path d="M3 6h6M6 3c-1.4 1.8-1.4 4.2 0 6M6 3c1.4 1.8 1.4 4.2 0 6" stroke="var(--gold)" stroke-width=".6" fill="none"/></svg>
        www.tinmarrowseek.com
      </li>
    </ul>

    <p class="holder-name">Odel Krasniak</p>

    <address class="address" style="font-style: normal;">
      7281 Porravel Blvd. Suite 382<br>
      Porravel Heights, CA 95555
    </address>

    <svg class="waves" viewBox="0 0 500 120" preserveAspectRatio="none" aria-hidden="true">
      <path d="M0 112 C120 118 220 100 320 74 C400 54 450 40 500 30 L500 120 L0 120 Z" fill="var(--cream-soft)"/>
      <path d="M0 118 C140 120 250 108 350 88 C420 74 465 66 500 62 L500 120 L0 120 Z" fill="var(--cream)"/>
      <path d="M0 104 C130 112 230 92 330 64 C410 42 460 28 500 20" stroke="var(--cream-soft)" stroke-width="1.2" fill="none"/>
    </svg>
  </section>
</main>
</body>
</html>
```